AMAZING WEBSITE DESIGN NEEDED FOR MAID / CLEANING SERVICE

NOTE: This is Website Design Only - No coding required

Please submit your designs ASAP as we want to pick a winner and get started!

Hey,

We are looking for a new amazing website design for a maid or cleaning service.

They have a horrible website that we want turned into a masterpiece.

As you will see on their current site:

http://tidyhavenco.examplehost.net/

They have a lot of stuff, very disorganized, and need help.

Here is what we need:

Colors: Same as current site, Orange, Gray, Black

Menu: Horizontal with same Menu items

Need a spot for a video on the homepage

Want content to be structured in a great format that is easy to read.

Want to highlight commercial and residential on the website homepage.

Also want a spot for customer testimonials

We want the site clean, professional, fresh and modern.

Please help by matching the logo design.

I look forward to your designs!
Updates

Hi All! Really appreciate your efforts and designs. I will be meeting with our client on Monday and will then be able to provide feedback after our meeting. If you have other ideas, please submit them. The more I can show him the better! Thanks!

Target Market(s)

The target market is residential home owners as well as commercial businesses who need cleaning on a regular basis.

This company cleans homes and offices for individuals.

Industry/Entity Type

Residential

Font styles to use
Sans Serif

Requirements
Must have
• Must match logo colors
Must have spot for video
Must have a clean look
Must have a bold look
Nice to have
• Highly visual
Should not have
• clutter
messy design
hard to read

```html
<!DOCTYPE html>
<html lang="en">
<head>
<meta charset="utf-8">
<title>Tidy Haven — Quality Commercial &amp; Residential Cleaning</title>
<link rel="stylesheet" href="https://fonts.googleapis.com/css2?family=Dosis:wght@400;500;600;700&family=Open+Sans:ital,wght@0,400;0,600;1,400&display=swap">
<style>
:root{
  --orange:#f47b16;
  --orange-dark:#e06c0c;
  --gray:#8a8a8a;
  --gray-dark:#6f6f6f;
  --ink:#111;
  --paper:#f4f4f4;
  --white:#fff;
}
*{margin:0;padding:0;box-sizing:border-box}
html,body{width:916px;height:1200px;overflow:hidden;background:var(--white)}
body{position:relative;font-family:"Open Sans",Verdana,sans-serif;color:var(--ink)}
h1,h2{font-weight:400}
.abs{position:absolute}

/* header */
.topline{left:0;top:0;width:916px;height:4px;background:var(--gray-dark)}
.header{left:0;top:4px;width:916px;height:114px;background:var(--paper)}
.brand{left:198px;top:52px;display:flex;align-items:center;gap:10px}
.brand-square{width:26px;height:26px;background:var(--orange)}
.brand-name{font-family:"Dosis",sans-serif;font-weight:700;font-size:34px;color:var(--orange);line-height:1}
.brand-tag{left:234px;top:92px;font-family:"Dosis",sans-serif;font-weight:600;font-size:11px;color:var(--gray-dark)}
.utility{right:198px;top:12px;font-family:"Dosis",sans-serif;font-weight:600;font-size:12px;color:var(--orange);letter-spacing:.3px;word-spacing:1px}
.utility span{color:var(--orange);margin:0 6px}
.help{right:198px;top:40px;font-style:italic;font-size:11px;color:var(--ink)}
.phone{right:198px;top:53px;font-size:19px;color:var(--ink)}
.search{left:641px;top:84px;width:77px;height:19px;border-radius:10px;background:var(--orange)}
.search svg{position:absolute;right:6px;top:3px}

/* nav */
.nav{left:0;top:118px;width:916px;height:30px;background:var(--orange)}
.nav a{position:absolute;top:0;height:30px;line-height:30px;font-family:"Dosis",sans-serif;font-weight:500;font-size:12px;color:var(--white);text-decoration:none;letter-spacing:.3px}
.nav a.current{background:var(--gray);padding:0 12px}

/* hero */
.hero{left:0;top:148px;width:916px;height:252px;background:linear-gradient(90deg,#4a4441 0%,#bdb6ad 22%,#e7e2da 45%,#d9b79c 52%,#efece7 66%,#f6f5f2 100%)}
.hero-title{left:200px;top:200px;font-family:"Dosis",sans-serif;font-size:19px;line-height:21px;color:var(--ink);letter-spacing:.5px}
.dots{left:692px;top:386px;display:flex;gap:4px}
.dots i{width:6px;height:6px;border-radius:50%;background:var(--orange)}
.dots i:first-child{background:var(--white)}

/* features */
.features{left:0;top:400px;width:916px;height:193px;background:var(--gray)}
.feature{position:absolute;top:426px;width:150px}
.feature-num{position:absolute;left:0;top:-2px;font-family:"Dosis",sans-serif;font-size:40px;line-height:36px;color:var(--orange)}
.feature-title{position:absolute;left:20px;top:0;font-family:"Dosis",sans-serif;font-size:14px;line-height:16px;color:var(--ink);white-space:nowrap}
.feature-lead{position:absolute;left:0;top:40px;width:150px;font-style:italic;font-size:7.4px;line-height:9.5px;color:var(--white)}
.feature-body{position:absolute;left:0;top:79px;width:134px;font-size:7.4px;line-height:9.5px;color:var(--ink)}
.btn{position:absolute;display:block;height:21px;line-height:21px;text-align:center;font-size:8px;color:var(--white);text-decoration:none;border-radius:2px}
.btn-orange{background:var(--orange);width:56px}
.btn-black{background:var(--ink);width:55px}

/* welcome */
.welcome{left:0;top:593px;width:916px;height:185px;background:var(--paper)}
.welcome-title{left:198px;top:618px;font-family:"Dosis",sans-serif;font-size:20px;color:var(--ink);letter-spacing:.4px}
.welcome-text{left:198px;top:654px;width:368px;font-size:7.4px;line-height:10px;color:var(--orange)}
.welcome-photo{left:566px;top:618px;width:166px;height:152px;background:radial-gradient(ellipse at 50% 45%,#e9d6c3 0%,#e8eef0 45%,#f4f4f4 75%)}

/* testimonials + video */
.band{left:0;top:778px;width:916px;height:264px;background:var(--orange)}
.band-title{top:804px;font-family:"Dosis",sans-serif;font-size:20px;color:var(--white);letter-spacing:.4px}
.date{position:absolute;left:198px;width:34px;height:54px;background:var(--ink);color:var(--white);text-align:center;font-family:"Dosis",sans-serif}
.date b{display:block;font-weight:500;font-size:20px;line-height:22px;margin-top:6px;color:var(--orange)}
.date small{display:block;font-size:8px;letter-spacing:.3px}
.quote-name{position:absolute;left:244px;font-family:"Dosis",sans-serif;font-size:10px;color:var(--ink)}
.quote-text{position:absolute;left:244px;width:200px;font-size:7.6px;line-height:10px;color:var(--ink)}
.video{left:472px;top:840px;width:246px;height:148px;background:linear-gradient(135deg,#5c5c5c,#3e3e3e 60%,#555)}
.video-bar{position:absolute;left:0;bottom:0;width:246px;height:10px;background:#ddd}
.spinner{position:absolute;left:115px;top:62px}

/* footer */
.footer{left:0;top:1042px;width:916px;height:158px;background:#000}
.foot-links{position:absolute;top:1076px;list-style:none;font-family:"Dosis",sans-serif;font-weight:600;font-size:10px;line-height:15px;color:var(--white)}
.follow{left:560px;top:1075px;font-size:8px;color:var(--white)}
.social{position:absolute;top:1066px;width:18px;height:18px;background:var(--orange)}
.address{left:560px;top:1094px;font-size:7.6px;line-height:9.6px;color:var(--white);font-style:normal}
.copyright{left:198px;top:1164px;font-size:7.6px;color:var(--white)}
</style>
</head>
<body>

<div class="abs topline"></div>
<header class="abs header"></header>
<div class="abs brand"><span class="brand-square"></span><span class="brand-name">Tidy Haven</span></div>
<div class="abs brand-tag">Quality Commercial &amp; Residential Cleaning</div>
<div class="abs utility">SPECIAL OFFERS<span>|</span>REQUEST A BID<span>|</span>MEET THE PRESIDENT &amp; CEO</div>
<div class="abs help">If you need help, call us instantly</div>
<div class="abs phone">(505) 555-0142</div>
<div class="abs search">
  <svg width="12" height="12" viewBox="0 0 12 12"><circle cx="5" cy="5" r="3.5" fill="none" stroke="#fff" stroke-width="1.6"/><line x1="7.6" y1="7.6" x2="11" y2="11" stroke="#fff" stroke-width="1.8"/></svg>
</div>

<nav class="abs nav">
  <a class="current" style="left:198px">HOME</a>
  <a style="left:262px">ABOUT</a>
  <a style="left:318px">SERVICES</a>
  <a style="left:390px">EMPLOYEES</a>
  <a style="left:472px">WHY CHOOSE US</a>
  <a style="left:571px">TESTIMONIALS</a>
  <a style="left:663px">CONTACT</a>
</nav>

<section class="abs hero" role="img" aria-label="Smiling cleaner holding a caddy of cleaning supplies and a duster in a bright living room"></section>
<div class="abs hero-title">RESIDENTIAL &amp;<br>COMMERCIAL</div>
<div class="abs dots"><i></i><i></i><i></i></div>

<section class="abs features"></section>
<div class="feature" style="left:198px">
  <div class="feature-num">1</div>
  <div class="feature-title">Locally Owned<br>&amp; Operated</div>
  <p class="feature-lead">Never deal with an unresponsive franchise - Deal with the owner!</p>
  <p class="feature-body">This is a company designed around the customer! We will make sure that you are accomodated in every way possible.</p>
  <a class="btn btn-orange" style="top:119px">Read More</a>
</div>
<div class="feature" style="left:388px">
  <div class="feature-num">2</div>
  <div class="feature-title">Residential<br>&amp; Commercial</div>
  <p class="feature-lead">Office Buildings - Car Dealerships - Party Set-up &amp; Clean-up - Parking lot Cleaning - RV's - Warehouse.....we do it ALL!</p>
  <p class="feature-body">This is a company designed around the customer! We will make sure that you are accomodated in every way possible.</p>
  <a class="btn btn-orange" style="top:119px">Read More</a>
</div>
<div class="feature" style="left:569px">
  <div class="feature-num">3</div>
  <div class="feature-title">Services Provided<br>&amp; Efficiency in work</div>
  <p class="feature-lead">First Impressions are everything!! They will make you or break you.</p>
  <p class="feature-body">This is a company designed around the customer! We will make sure that you are accomodated in every way possible.</p>
  <a class="btn btn-orange" style="top:119px">Read More</a>
</div>

<section class="abs welcome"></section>
<h1 class="abs welcome-title">WELCOME TO TIDY HAVEN</h1>
<p class="abs welcome-text">Thank you for visiting us! You are one step closer to experiencing first class maid service! Our company specializes in detailed housekeeping, janitorial, and commercial cleaning services making your environment shine and sparkle like it never has before! Our maids are fully trained professionals who we recruit from high end luxury hotels we know, like the Grand Aster and Bellmont! We pride ourselves in delivering exceptional service to our valued customers by fully understanding what your expectations &amp; needs are! We will strive for perfection and we will provide an uncompromising commitment to excellence! Our "all-inclusive" promise gives us an edge over our competition by giving you access to more home and office cleaning services for absolutely no extra costs! Why pay more for less?? NEVER have any hidden charges, overages, or sneaky fees! With Tidy Haven start getting more for your dollar! Your wish is our command and that is the true Tidy Haven way! Call us today!</p>
<div class="abs welcome-photo" role="img" aria-label="Cleaner in yellow gloves kneeling and wiping the floor beside a blue bucket"></div>

<section class="abs band"></section>
<h2 class="abs band-title" style="left:198px">TESTIMONIALS</h2>
<div class="date" style="top:840px"><b>02</b><small>JAN '14</small></div>
<div class="quote-name" style="top:838px">Dylan Mercer</div>
<p class="quote-text" style="top:856px">"I was very impressed with the amount they do for the price! Remarkable! Thank you Tidy Haven for taking this daily headache away from my fiance. She was so thrilled. See you guys again soon!</p>
<div class="date" style="top:912px"><b>21</b><small>DEC '13</small></div>
<div class="quote-name" style="top:910px">Joanna Whitfield</div>
<p class="quote-text" style="top:928px">"Thank you Tidy Haven for making my house so fresh and clean! How nice it was to have all of my laundry washed and folded and my dishes done &amp; put away along with everything else! I have requested that she return next week! Oustanding you guys, keep it up!</p>
<a class="btn btn-black" style="left:243px;top:996px">Read More</a>

<h2 class="abs band-title" style="left:472px">HOW DOES IT WORKS?</h2>
<div class="abs video" role="img" aria-label="Video player showing a cleaner scrubbing a floor beside a red bucket">
  <svg class="spinner" width="16" height="16" viewBox="0 0 16 16"><circle cx="8" cy="8" r="6" fill="none" stroke="#ccc" stroke-width="2" stroke-dasharray="4 3"/></svg>
  <div class="video-bar"></div>
</div>

<footer class="abs footer"></footer>
<ul class="foot-links" style="left:198px"><li>HOME</li><li>SERVICES</li><li>ABOUT</li><li>EMPLOYEES</li><li>WHY CHOOSE US</li></ul>
<ul class="foot-links" style="left:304px"><li>TESTIMONIALS</li><li>REQUEST A BID</li><li>SPECIAL OFFERS</li><li>CONTACT US</li><li>MEET THE PRESIDENTS &amp; CEO</li></ul>
<div class="abs follow">Follow Us At</div>
<span class="social" style="left:616px"></span>
<span class="social" style="left:638px"></span>
<address class="abs address">Tidy Haven<br>4120 Mesa Verde Road NE Suite 210<br>Riverton | New Mexico | 87000<br>(505) 555-0142 Office<br>(505) 555-0187 Fax<br>info@tidyhaven.example</address>
<div class="abs copyright">Tidy Haven © 2014 | Privacy Policy</div>

</body>
</html>
```